Security Camera Sign

14” high x 11” wide Color: Blue, Yellow, Black and white

Make the sign vertical
Replace red with blue
WARNING: Black over yellow
These premises are protected by Closed Circuit Television: On white
Images are recorded for crime prevention and public safety. Unauthorized access, theft or vandalism will result in prosecution: On Blue

Target Market(s)

Outdoor commercial building

Industry/Entity Type

Security

Requirements
Nice to have
• I would like the sign stand out. If you need more colors? Thanks Ok

```html
<!DOCTYPE html>
<html lang="en">
<head>
<meta charset="utf-8">
<title>CCTV Warning Sign</title>
<link rel="stylesheet" href="https://fonts.googleapis.com/css2?family=Montserrat:wght@800;900&family=Open+Sans:wght@800&family=Fira+Sans+Extra+Condensed:wght@600;700;800&display=swap">
<style>
  :root {
    --sign-blue: #1a6fe0;
    --warning-yellow: #fff200;
    --ink: #0b0b0b;
    --paper: #ffffff;
    --alert-red: #f2101a;
    --camera-light: #eceef0;
    --camera-shade: #b9bdc2;
  }
  * { margin: 0; padding: 0; box-sizing: border-box; }
  html, body {
    width: 943px;
    height: 1200px;
    overflow: hidden;
    background: var(--paper);
  }
  .sign {
    position: absolute;
    left: 26px;
    top: 30px;
    width: 891px;
    height: 1143px;
    border: 5px solid var(--ink);
    border-radius: 32px;
    overflow: hidden;
    background: var(--paper);
  }
  .header-band {
    position: absolute;
    left: 0; top: 0;
    width: 100%;
    height: 286px;
    background: var(--sign-blue);
  }
  .warning-plate {
    position: absolute;
    left: 50px;
    top: 41px;
    width: 776px;
    height: 196px;
    background: var(--warning-yellow);
    border: 5px solid var(--ink);
    border-radius: 32px;
  }
  .warning-plate svg { display: block; width: 100%; height: 100%; }
  .warning-word {
    font-family: 'Montserrat', sans-serif;
    font-weight: 900;
    fill: var(--ink);
  }
  .notice {
    position: absolute;
    left: 47px;
    top: 322px;
    font-family: 'Open Sans', sans-serif;
    font-weight: 800;
    font-size: 58px;
    line-height: 68.5px;
    color: var(--ink);
    letter-spacing: -0.5px;
    text-shadow: 2px 2px 2px rgba(0,0,0,0.35);
  }
  .notice span { display: block; }
  .camera-visual {
    position: absolute;
    left: 350px;
    top: 330px;
    width: 520px;
    height: 530px;
    border-radius: 40px;
    background: radial-gradient(ellipse at 55% 40%, var(--camera-light) 0%, #e2e4e7 45%, rgba(255,255,255,0) 75%);
  }
  .footer-band {
    position: absolute;
    left: 0;
    top: 898px;
    width: 100%;
    height: 250px;
    background: var(--sign-blue);
  }
  .footer-band svg { display: block; width: 100%; height: 100%; }
  .footer-line {
    font-family: 'Fira Sans Extra Condensed', sans-serif;
    font-weight: 700;
  }
  .recording-note { fill: var(--paper); font-weight: 600; }
  .offence-list { fill: var(--paper); }
  .consequence { fill: var(--alert-red); font-weight: 800; }
</style>
</head>
<body>
  <main class="sign">
    <section class="header-band">
      <div class="warning-plate">
        <svg viewBox="0 0 766 186" aria-label="Warning">
          <text class="warning-word" x="383" y="148" text-anchor="middle" font-size="150" textLength="700" lengthAdjust="spacingAndGlyphs">WARNING</text>
        </svg>
      </div>
    </section>

    <p class="notice">
      <span>THESE</span>
      <span>PREMISES</span>
      <span>ARE</span>
      <span>PROTECTED</span>
      <span>BY</span>
      <span>CLOSED</span>
      <span>CIRCUIT</span>
      <span>TELEVISION</span>
    </p>

    <div class="camera-visual" role="img" aria-label="White wall-mounted CCTV security camera in a weatherproof housing"></div>

    <section class="footer-band">
      <svg viewBox="0 0 881 250">
        <text class="footer-line recording-note" x="29" y="58" font-size="38" textLength="820" lengthAdjust="spacingAndGlyphs">Images are recorded for crime prevention and public safety</text>
        <text class="footer-line offence-list" x="29" y="136" font-size="56" textLength="820" lengthAdjust="spacingAndGlyphs">UNAUTHORIZED ACCESS, THEFT OR VANDALISM</text>
        <text class="footer-line consequence" x="28" y="206" font-size="80" textLength="822" lengthAdjust="spacingAndGlyphs">WILL RESULT IN PROSECUTION</text>
      </svg>
    </section>
  </main>
</body>
</html>
```